New Business Card Design Project

I would like to purchase a customized version of a design you have previously submitted - https://www.plorvexa.com/design/7314826<br/><br/>I would like to incorporate the attached Images for my fitness company "TrelmoKor Athletics". My initial services is personal training and athletic performance. I would like a card that has one a shiny black side with the silver logo and the side with a white background utilizing the gold logo. On the white side, put "Sports Performance and Functional Strength Training" under the logo.
Industry/Entity Type
Fitness
Contact Information for Business Card
Quillan Morrow
Owner and Trainer
555.271.9384
quillan.morrow@trelmokorathletics.com
Look and feel
Each slider illustrates characteristics of the customer's brand and the style your logo design should communicate.

```html
<!DOCTYPE html>
<html lang="en">
<head>
<meta charset="UTF-8">
<title>TrelmoKor Athletics – Business Card</title>
<link href="https://fonts.googleapis.com/css2?family=Montserrat:wght@500;600;700&display=swap" rel="stylesheet">
<style>
  :root {
    --backdrop: #2b2b2d;
    --card-black: #0b0b0c;
    --card-white: #ffffff;
    --silver: #c9cacc;
    --gold: #9c8558;
    --ink: #1c1c1c;
    --muted: #555555;
    --divider: #3a3a3a;
  }
  * { margin: 0; padding: 0; box-sizing: border-box; }
  html, body {
    width: 1200px;
    height: 880px;
    overflow: hidden;
    background: var(--backdrop);
    font-family: "Montserrat", sans-serif;
  }
  .canvas {
    width: 1200px;
    height: 880px;
    display: flex;
    flex-direction: column;
    align-items: center;
    justify-content: center;
    gap: 40px;
  }
  .card {
    width: 640px;
    height: 366px;
    position: relative;
    overflow: hidden;
    box-shadow: 0 10px 30px rgba(0,0,0,0.45);
  }
  .card--front {
    background: linear-gradient(135deg, #1a1a1c 0%, var(--card-black) 55%, #000 100%);
    display: flex;
    align-items: center;
    justify-content: center;
  }
  .brand {
    display: flex;
    align-items: center;
    gap: 14px;
    font-weight: 700;
    letter-spacing: 0.08em;
    text-transform: uppercase;
  }
  .brand__dot { border-radius: 50%; flex: none; }
  .brand--silver { color: var(--silver); font-size: 24px; }
  .brand--silver .brand__dot { width: 30px; height: 30px; border: 3px solid var(--silver); }
  .brand--gold {
    color: var(--gold);
    font-size: 18px;
    flex-direction: column;
    gap: 10px;
    text-align: center;
    line-height: 1.25;
  }
  .brand--gold .brand__dot { width: 26px; height: 26px; border: 3px solid var(--gold); }

  .card--back { background: var(--card-white); }
  .back__brand {
    position: absolute;
    left: 30px;
    top: 92px;
    width: 180px;
    display: flex;
    justify-content: center;
  }
  .back__divider {
    position: absolute;
    left: 230px;
    top: 78px;
    width: 2px;
    height: 140px;
    background: var(--divider);
  }
  .contact {
    position: absolute;
    left: 254px;
    top: 82px;
    color: var(--ink);
  }
  .contact__name {
    font-size: 21px;
    font-weight: 700;
    margin-bottom: 4px;
  }
  .contact__title {
    font-size: 13px;
    font-weight: 500;
    color: var(--muted);
    margin-bottom: 18px;
  }
  .contact__line {
    display: flex;
    align-items: center;
    gap: 10px;
    font-size: 14px;
    font-weight: 500;
    margin-bottom: 8px;
    white-space: nowrap;
  }
  .contact__line svg { flex: none; }
  .tagline {
    position: absolute;
    left: 40px;
    bottom: 58px;
    font-size: 15px;
    font-weight: 600;
    color: var(--ink);
    white-space: nowrap;
  }
</style>
</head>
<body>
  <main class="canvas">
    <section class="card card--front">
      <div class="brand brand--silver">
        <span class="brand__dot"></span>
        <span>TrelmoKor Athletics</span>
      </div>
    </section>

    <section class="card card--back">
      <div class="back__brand">
        <div class="brand brand--gold">
          <span class="brand__dot"></span>
          <span>TrelmoKor<br>Athletics</span>
        </div>
      </div>
      <div class="back__divider"></div>
      <div class="contact">
        <p class="contact__name">Quillan Morrow</p>
        <p class="contact__title">Owner and Trainer</p>
        <p class="contact__line">
          <svg width="14" height="14" viewBox="0 0 14 14" aria-hidden="true"><rect x="1.5" y="1.5" width="11" height="11" fill="none" stroke="#1c1c1c" stroke-width="1.6"/></svg>
          555.271.9384
        </p>
        <p class="contact__line">
          <svg width="14" height="12" viewBox="0 0 14 12" aria-hidden="true"><rect x="0.5" y="1" width="13" height="10" fill="#1c1c1c"/><path d="M1 1.5 L7 6.5 L13 1.5" fill="none" stroke="#fff" stroke-width="1.2"/></svg>
          quillan.morrow@trelmokorathletics.com
        </p>
      </div>
      <p class="tagline">Sports Performance and Functional Strength Training</p>
    </section>
  </main>
</body>
</html>
```